Harlow Creekside Clinic Tri-Fold Flyer

a marketing 3- fold flyer for primary business awareness. this should offer all aspects of our medical practice. I have provided several pictures as well as all pertinent information needed to make a successful flyer. This needs to be eye catching and attractive. each page should feature something of its own.
my thoughts:
page 1- photo of office our mission statement and maybe our phone number and address
page 2- our HCC A-team flyer
page 3- our paragraph on our practice as well as some of our services. say something like we offer a wide scope of services including health coaching, weight loss. A "patient services coordinator" will help you pick out what services we can do for you. a pic
page 4- doctors bio and pics and logos
page 5-
page 6- our map our address and phone numbers. the sentence on making an appointment. our web page and facebook as well as our logos

Target Market(s)

we are a medical practice, so we are seeking new patients

Industry/Entity Type

Health Care

Font styles to use
Serif

Colors
34a6d7
33b8a4
abd036
fbee3e

Requirements
Must have
• I have enclosed a tri-fold info attachment as well as other pieces. Use what you feel will make our flyer attractive. Not too busy. Please try to get most info in
• All work purchased should be delivered with the PDF form for future changes by owner of medical office.
Nice to have
• All Info provided

```html
<!DOCTYPE html>
<html lang="en">
<head>
<meta charset="utf-8">
<title>Harlow Creekside Clinic Tri-Fold Flyer</title>
<link href="https://fonts.googleapis.com/css2?family=Montserrat:ital,wght@0,300;0,400;0,600;0,700;1,400;1,600&display=swap" rel="stylesheet">
<style>
  :root {
    --navy: #1d3557;
    --ink: #1f2a44;
    --green: #8dbb2f;
    --lime: #abd036;
    --teal: #2a9a96;
    --teal-dark: #1f6f7a;
    --blue: #5b8fc9;
    --sky: #8cbde0;
    --paper: #ffffff;
    --stage: #d4d4d4;
  }
  * { box-sizing: border-box; margin: 0; padding: 0; }
  html, body { width: 1200px; height: 960px; overflow: hidden; }
  body {
    background: var(--stage);
    font-family: "Montserrat", sans-serif;
    color: var(--ink);
  }
  .spread {
    position: absolute; left: 60px; top: 100px;
    width: 1080px; height: 760px;
    display: flex;
    box-shadow: 0 10px 30px rgba(0,0,0,.18);
  }
  .panel { position: relative; width: 360px; height: 760px; overflow: hidden; background: var(--paper); }

  /* Panel 1 */
  .panel-team .decor { position: absolute; inset: 0; }
  .team-block { position: absolute; left: 96px; top: 100px; width: 200px; }
  .team-title { font-size: 30px; font-weight: 700; font-style: italic; color: var(--lime); margin-bottom: 6px; }
  .team-list { list-style: none; font-size: 10.5px; line-height: 1.35; }
  .team-list li::before { content: "• "; }
  .pride { position: absolute; left: 34px; top: 488px; width: 300px; color: #fff; }
  .pride h2 { font-size: 19px; font-weight: 700; line-height: 1.25; margin-bottom: 10px; }
  .pride p { font-size: 13px; font-weight: 300; line-height: 1.35; }

  /* Panel 2 */
  .diagram { position: absolute; left: 0; top: 4px; width: 360px; height: 300px; }
  .intro { position: absolute; left: 26px; top: 312px; width: 310px; font-size: 9.8px; font-style: italic; line-height: 1.35; }
  .insurance { position: absolute; left: 0; width: 360px; top: 500px; text-align: center; color: var(--green); font-size: 10.5px; font-weight: 600; font-style: italic; }
  .services-band {
    position: absolute; left: 0; top: 530px; width: 360px; height: 230px;
    background: linear-gradient(180deg, #6aa3d8, #8cc0e6);
    display: flex; gap: 10px; padding: 14px 12px; color: #fff;
  }
  .svc-col { flex: 1; }
  .svc-col h3 { font-size: 9.5px; font-weight: 700; font-style: italic; margin-bottom: 3px; letter-spacing: .3px; }
  .svc-col ul { list-style: none; font-size: 8.8px; font-style: italic; line-height: 1.4; }
  .svc-col li::before { content: "• "; }

  /* Panel 3 */
  .doc-lead { position: absolute; left: 0; top: 0; width: 360px; height: 300px; background: var(--navy); color: #fff; }
  .doc-second { position: absolute; left: 0; top: 300px; width: 360px; height: 230px; background: var(--green); }
  .doc-photo { position: absolute; width: 112px; height: 112px; background: linear-gradient(135deg, #7a6a5c, #3b3430); }
  .doc-lead .doc-photo { left: 24px; top: 24px; }
  .doc-second .doc-photo { right: 24px; top: 74px; background: linear-gradient(135deg, #9aa08e, #4d4a44); }
  .doc-name { font-size: 19px; font-weight: 700; }
  .doc-lead .doc-name { position: absolute; left: 152px; top: 92px; color: var(--lime); }
  .doc-bio { position: absolute; left: 24px; top: 146px; width: 316px; font-size: 10px; line-height: 1.4; font-weight: 300; }
  .doc-second .doc-name { position: absolute; left: 24px; top: 26px; color: var(--navy); }
  .doc-note { position: absolute; left: 24px; top: 56px; font-size: 11px; color: var(--navy); }
  .extra-band {
    position: absolute; left: 0; top: 530px; width: 360px; height: 230px;
    background: linear-gradient(180deg, #5c8dc6, #4f7fbd);
    display: flex; gap: 14px; padding: 16px 20px; color: #fff;
  }
  .extra-band h3 { font-size: 10.5px; font-weight: 700; letter-spacing: .5px; margin-bottom: 5px; }
  .extra-band ul { list-style: none; font-size: 10px; line-height: 1.4; font-weight: 300; }
  .extra-band li::before { content: "• "; }
  .extra-col { flex: 1; }
</style>
</head>
<body>
<main class="spread">

  <section class="panel panel-team">
    <svg class="decor" viewBox="0 0 360 760" aria-hidden="true">
      <defs>
        <linearGradient id="tealBand" x1="0" y1="0" x2="1" y2="1">
          <stop offset="0" stop-color="#1f6f7a"/><stop offset="1" stop-color="#3aa8a0"/>
        </linearGradient>
        <linearGradient id="blueBase" x1="0" y1="0" x2="0" y2="1">
          <stop offset="0" stop-color="#4f86c4"/><stop offset="1" stop-color="#7fb3e0"/>
        </linearGradient>
      </defs>
      <polygon points="40,0 360,0 360,30 130,70" fill="#abd036"/>
      <polygon points="110,0 360,40 360,110 230,90" fill="#8dbb2f" opacity=".85"/>
      <polygon points="230,90 360,60 360,120" fill="#6cb23a"/>
      <polygon points="0,260 40,250 360,470 360,520" fill="#5b96d2" opacity=".9"/>
      <polygon points="0,300 360,520 360,560 0,330" fill="#8cbde0" opacity=".7"/>
      <line x1="0" y1="295" x2="360" y2="340" stroke="#c8e07a" stroke-width="2"/>
      <line x1="0" y1="303" x2="360" y2="348" stroke="#c8e07a" stroke-width="2"/>
      <line x1="0" y1="311" x2="360" y2="356" stroke="#dcebaa" stroke-width="2"/>
      <polygon points="0,440 360,440 360,630 0,660" fill="url(#tealBand)"/>
      <polygon points="0,660 360,630 360,760 0,760" fill="url(#blueBase)"/>
    </svg>
    <div class="team-block">
      <h2 class="team-title">A team</h2>
      <ul class="team-list">
        <li>Medical personnel to treat your medical issues</li>
        <li>Health/Wellness &amp; Fitness staff to complete process to guide you to be disease FREE</li>
        <li>Will work with your insurance</li>
        <li>Will develop a NATURAL alternative approach to health care</li>
      </ul>
    </div>
    <div class="pride">
      <h2>At HCC, LLC we take pride in providing the finest wellness care to our patients</h2>
      <p>Listed here are some of the services we provide in our Millbrook office</p>
    </div>
  </section>

  <section class="panel panel-approach">
    <svg class="diagram" viewBox="0 0 360 300" role="img" aria-label="Integrative care approach diagram">
      <g fill="none" stroke-width="1.6">
        <circle cx="180" cy="150" r="50" stroke="#8dbb2f"/>
        <circle cx="105" cy="62" r="34" stroke="#1d3557"/>
        <circle cx="200" cy="40" r="34" stroke="#8dbb2f"/>
        <circle cx="285" cy="72" r="34" stroke="#8dbb2f"/>
        <circle cx="300" cy="160" r="34" stroke="#8dbb2f"/>
        <circle cx="250" cy="240" r="34" stroke="#8dbb2f"/>
        <circle cx="150" cy="262" r="34" stroke="#8dbb2f"/>
        <circle cx="55" cy="225" r="34" stroke="#1d3557"/>
        <circle cx="52" cy="135" r="34" stroke="#1d3557"/>
      </g>
      <g stroke="#8dbb2f" stroke-width="1.2">
        <line x1="180" y1="100" x2="195" y2="74"/>
        <line x1="220" y1="120" x2="255" y2="90"/>
        <line x1="230" y1="152" x2="266" y2="158"/>
        <line x1="212" y1="188" x2="232" y2="212"/>
        <line x1="168" y1="198" x2="158" y2="228"/>
      </g>
      <g stroke="#1d3557" stroke-width="1.2">
        <line x1="150" y1="110" x2="124" y2="90"/>
        <line x1="130" y1="150" x2="86" y2="140"/>
        <line x1="140" y1="180" x2="86" y2="212"/>
      </g>
      <g font-family="Montserrat, sans-serif" font-size="7.5" font-style="italic" text-anchor="middle" fill="#1f2a44">
        <text x="180" y="136">Integrative</text><text x="180" y="146">Health Care</text>
        <text x="180" y="156">Approach with</text><text x="180" y="166">Health / Wellness</text>
        <text x="180" y="176">&amp; Fitness Solutions</text>
        <text x="105" y="60">Primary</text><text x="105" y="70">Dr Care</text>
        <text x="200" y="34">Health &amp;</text><text x="200" y="43">Wellness</text><text x="200" y="52">Coaching</text>
        <text x="285" y="70">Nutritional</text><text x="285" y="80">Counseling</text>
        <text x="300" y="158">Fitness</text><text x="300" y="168">Training</text>
        <text x="250" y="238">Weight</text><text x="250" y="248">Management</text>
        <text x="150" y="260">Smoking</text><text x="150" y="270">Cessation</text>
        <text x="55" y="223">Outpatient</text><text x="55" y="233">Care</text>
        <text x="52" y="128">In-house</text><text x="52" y="138">Clinical</text><text x="52" y="148">Services</text>
      </g>
    </svg>
    <p class="intro">Our physicians serving Millbrook and the surrounding area. Our doctors and the rest of the welcoming team at Harlow Creekside Clinic, LLC are committed to providing integrative medical solutions to address your unique needs, whether you are experiencing back pain, knee pain, or even muscular tightness and tension. You may be searching for pain relief after an accident, experiencing an injury, or if you suffer from a specific condition like chronic back pain or knee pain. Even if you are looking to improve your overall health &amp; nutrition, our doctor can help you attain your everyday wellness goals!</p>
    <p class="insurance">We accept most major insurances</p>
    <div class="services-band">
      <div class="svc-col">
        <h3>CLINICAL</h3>
        <ul><li>primary care</li><li>Vaccinations</li><li>Adult care</li><li>Geriatric care</li><li>routine wellness</li><li>pediatrics</li><li>GYN routine care</li><li>transition of care</li></ul>
      </div>
      <div class="svc-col">
        <h3>WELLNESS</h3>
        <ul><li>IV nutritional infusions / Iron &amp; Vit. C</li><li>Meyer's cocktail infusions</li><li>womans preventive care</li><li>mens preventive care</li><li>health Coaching</li><li>Anti-Aging prevention</li><li>Life style advice /counseling</li><li>Nutritional coaching</li></ul>
      </div>
      <div class="svc-col">
        <h3>FITNESS &amp; WEIGHT</h3>
        <ul><li>personal weight loss</li><li>meal preps</li><li>cooking classes</li><li>seminars</li><li>protein supplements</li><li>AMPK</li><li>corrective excercises</li><li>gym acces</li><li>personal trainer</li></ul>
      </div>
    </div>
  </section>

  <section class="panel panel-doctors">
    <div class="doc-lead">
      <div class="doc-photo" role="img" aria-label="Portrait photo of Dr. Marcus Lian"></div>
      <h2 class="doc-name">Dr. Marcus Lian</h2>
      <p class="doc-bio">Dr. Marcus Lian served in the U.S. Army as a commander and flight surgeon. He specialized in combat medicine, wound care and rehabilitation. His goals were to maintain the health and fitness of Army soldiers. He developed an integrative approach to medicine and fitness. He believes that the body was engineered for fitness. Dr. Lian founded Harlow Creekside Clinic. Dr. Lian has 9 years of medical training and expertise as well as a genuine passion for healthcare. He is a graduate of Ashbury University where he received his doctorate.</p>
    </div>
    <div class="doc-second">
      <h2 class="doc-name">Dr. Elliot</h2>
      <p class="doc-note">text not found</p>
      <div class="doc-photo" role="img" aria-label="Portrait photo of Dr. Elliot"></div>
    </div>
    <div class="extra-band">
      <div class="extra-col">
        <h3>SPECIAL SERVICES</h3>
        <ul><li>metabolic syndrome</li><li>migraine treatment</li><li>botox for migraines</li><li>Lyme Disease</li><li>arthritis</li><li>low chronic back pain</li><li>MEND protocol</li><li>Pulminary rehab</li><li>Physciatric care/ behavioral - Minds &amp; Body</li><li>COPD</li><li>Chronic inflamation</li></ul>
      </div>
      <div class="extra-col">
        <h3>OUTPATIENT SERVICES</h3>
        <ul><li>Skin/Scar revisions</li><li>cancer biopsy</li><li>wound care</li><li>Collagen fillers</li><li>stem cell injections - PRP</li><li>Botox treatment for minor wrinkles</li></ul>
      </div>
    </div>
  </section>

</main>
</body>
</html>
```